"Thank You" card for professional property management agency.

We need to create a DL size "Thank You" card primarily used to thank new clients for their business and referrals.
We are a real estate agency based on Sydney's Northern Beaches. We want the card to feel happy and professional, incorporating our logo.
See our website for details about our business - www.harbourlanerealty.com.au
We have attached our logo in black text and white text as well as some images we have used across our website.
One side must have the ability to hand write a message of thank you on.
I would like this to be a clean and simple design, feel free to use any image supplied, but we are also happy with plain or patterned designs too.

Target Market(s)

Property investors male and female aged 30-60

Industry/Entity Type

Real Estate

Font styles to use
Other font styles liked:
• Please let the designer choose font

Colors

Designer to choose colors to be used in the design.

Requirements
Must have
• DL Size: Full Bleed 213x102mm. Doc size 210x99mm (horizontal)
• Harbour Lane Realty Logo
• Contact Details:
• info@harbourlanerealty.com.au
• Tel: 0493 716 258
• Level 1, 17 Wentmore Rd, Calderwood NSW 2532
• "Thank You" somewhere on the card
• Area or side to write message on.
• Design to be provided in editable photoshop PSD file and print ready PDF file
Nice to have
• Sleek professional design that feels "happy or grateful" as it is a thank you card
• Happy to use a plain colour or pattern on one side - it does not have to be an image provided, but feel free to design with either.
Should not have
• should not be too busy, keep it clean and simple.

```html
<!DOCTYPE html>
<html lang="en">
<head>
<meta charset="utf-8">
<title>Harbour Lane Realty – Thank You Card</title>
<link rel="stylesheet" href="https://fonts.googleapis.com/css2?family=Open+Sans:wght@400;600;700&family=Dancing+Script:wght@600&display=swap">
<style>
  :root {
    --teal: #177f8e;
    --teal-deep: #136f7c;
    --pattern-light: #eef4f6;
    --ink: #1b1b1b;
    --body-ink: #333;
    --paper: #ffffff;
    --backdrop: #ececee;
    --box-line: #c9c9c9;
  }
  * { box-sizing: border-box; margin: 0; padding: 0; }
  html, body { width: 1200px; height: 1200px; overflow: hidden; }
  body {
    background: var(--backdrop);
    font-family: "Open Sans", Arial, sans-serif;
    position: relative;
  }
  .card {
    position: absolute;
    top: 200px;
    width: 400px;
    height: 800px;
    overflow: hidden;
    box-shadow: 0 6px 18px rgba(0,0,0,0.12);
  }
  /* Front */
  .card-front { left: 180px; background: var(--paper); }
  .front-pattern {
    position: absolute; inset: 0 0 106px 0;
    background: var(--pattern-light);
  }
  .brand {
    position: absolute; top: 100px; left: 0; right: 0;
    display: flex; align-items: center; justify-content: center; gap: 10px;
  }
  .brand-mark { width: 14px; height: 14px; background: var(--teal); }
  .brand-name {
    font-weight: 700; font-size: 27px; letter-spacing: 0.3px;
    color: var(--ink); white-space: nowrap;
  }
  .thanks {
    position: absolute; top: 252px; left: 0; right: 0;
    text-align: center;
    font-family: "Dancing Script", cursive;
    font-weight: 600; font-size: 84px; color: var(--teal);
    line-height: 1;
  }
  .message-box {
    position: absolute; top: 370px; left: 20px; right: 20px; height: 194px;
    background: var(--paper);
    border: 1px solid var(--box-line);
    display: flex; align-items: center; justify-content: center;
    padding: 0 18px 22px;
  }
  .message-box p {
    font-size: 11.8px; line-height: 23px; color: var(--body-ink); text-align: center;
  }
  .contact-band {
    position: absolute; left: 0; right: 0; bottom: 0; height: 106px;
    background: var(--teal); color: #fff;
    display: flex; flex-direction: column; align-items: center; justify-content: center;
    gap: 4px; font-size: 12.5px;
  }
  .contact-line { display: flex; align-items: center; gap: 8px; white-space: nowrap; }
  .contact-phone { font-size: 15px; }
  .contact-line svg { display: block; }
  /* Back */
  .card-back { left: 620px; background: var(--teal); }
  .back-pattern { position: absolute; inset: 0; background: var(--teal-deep); opacity: 0.55; }
  .photo-strip {
    position: absolute; top: 60px; left: 0; right: 0; height: 150px;
    display: flex;
  }
  .photo { flex: 1; }
  .photo-homes { background: linear-gradient(160deg, #7fb7e0 0%, #5a7a5a 55%, #8a8f7c 100%); }
  .photo-harbour { background: linear-gradient(180deg, #8cc6ea 0%, #3f8fbd 35%, #0f4f8a 100%); }
</style>
</head>
<body>
  <section class="card card-front">
    <div class="front-pattern" role="img" aria-label="Faint light teal repeating leaf pattern"></div>
    <div class="brand">
      <span class="brand-mark"></span>
      <span class="brand-name">HARBOUR LANE REALTY</span>
    </div>
    <h1 class="thanks">Thank You</h1>
    <div class="message-box">
      <p>Lorem ipsum dolor sit amet, vide harum sed id, cu solum percipitur eum, cu choro forensibus cum. Voluptaria delicatissimi est ne, ut sed habemus pertinacia definiebas, quo nemore invenire eu.</p>
    </div>
    <footer class="contact-band">
      <div class="contact-line">Level 1, 17 Wentmore Rd, Calderwood NSW 2532</div>
      <div class="contact-line contact-phone">
        <svg width="18" height="18" viewBox="0 0 24 24" aria-hidden="true"><path fill="#fff" d="M6.6 10.8a15.1 15.1 0 0 0 6.6 6.6l2.2-2.2c.3-.3.7-.4 1-.2 1.1.4 2.3.6 3.6.6.6 0 1 .4 1 1V20c0 .6-.4 1-1 1A17 17 0 0 1 3 4c0-.6.4-1 1-1h3.5c.6 0 1 .4 1 1 0 1.3.2 2.5.6 3.6.1.3 0 .7-.2 1z"/></svg>
        <span>0493 716 258</span>
      </div>
      <div class="contact-line">
        <svg width="24" height="16" viewBox="0 0 24 16" aria-hidden="true"><rect x="1" y="1" width="22" height="14" fill="none" stroke="#fff" stroke-width="1.6"/><path d="M1 1l11 8 11-8" fill="none" stroke="#fff" stroke-width="1.6"/></svg>
        <span>info@harbourlanerealty.com.au</span>
      </div>
    </footer>
  </section>

  <section class="card card-back">
    <div class="back-pattern" role="img" aria-label="Teal repeating leaf pattern"></div>
    <div class="photo-strip">
      <div class="photo photo-homes" role="img" aria-label="Photo of modern terraced homes with gardens under blue sky"></div>
      <div class="photo photo-harbour" role="img" aria-label="Photo of a harbour with moored boats and a waterfront suburb"></div>
    </div>
  </section>
</body>
</html>
```